Website Development for quillmarsh.com.au

Build a new Wordpress/Responsive website for quillmarsh.com.au

Target Market(s)

Compliance Managers, Risk Managers, Information Security and Cyber Security Professionals, Chief Data/Digital Officers, Chief Operating/Financial Officers, Business Continuity Professionals, Disaster Recovery Planners, Small Business Owners, Local/Federal Government entities

Industry/Entity Type

Data Service

Coding

Coded - Design and coding required

Number of Pages Required

5+ page

Font styles to use
Sans Serif

Colors

Designer to choose colors to be used in the design.

Requirements
Must have
• 1. Site Structure: Home Page plus the following chapter-pages for a) Services b) About c) Resources d) Blog e) Contact Us
• 2. Prefer site to built on wordpress and we can purchase a theme if needed (we currently use The7 for other sites)
• 3. Blog needs to be wordpress based
• 4. We will host the site ourselves on our own servers
• 5. Responsive Design
Nice to have
• 1. Livechat capability/interface
• 2. Capability for marketing automation integration (such as hubspot, marketo, infusionsoft etc)
• 3. Capability for CRM integration (Salesforce)

```html
<!DOCTYPE html>
<html lang="en">
<head>
<meta charset="utf-8">
<title>Quillmarsh — Home</title>
<link rel="stylesheet" href="https://fonts.googleapis.com/css2?family=Mulish:wght@400;600;700&display=swap">
<style>
:root{
  --red:#e01b2f;
  --dark:#1c1c1e;
  --ink:#333333;
  --muted:#555555;
  --line:#cfcfcf;
  --soft:#ececec;
  --panel:#e4e4e4;
  --white:#ffffff;
}
*{box-sizing:border-box;margin:0;padding:0}
html,body{width:1200px;height:3197px;overflow:hidden}
body{position:relative;font-family:"Mulish",Arial,sans-serif;color:var(--ink);background:var(--white)}
h2,h3{font-weight:400}
.abs{position:absolute}
/* header */
.site-header{left:0;top:0;width:1200px;height:83px;background:var(--white)}
.brand{left:145px;top:22px;display:flex;align-items:center;gap:8px;font-weight:700;font-size:24px;color:var(--red)}
.brand-mark{width:16px;height:16px;background:var(--red)}
.main-nav{top:30px;left:0;width:1200px;font-size:16px;color:#555}
.main-nav span{position:absolute;white-space:nowrap}
.main-nav .current{color:var(--red)}
/* hero */
.hero{left:0;top:83px;width:1200px;height:531px;background:linear-gradient(120deg,#3b6a8f 0%,#6f8ea6 35%,#4d5a66 60%,#2a2f36 100%)}
.hero-caption{left:330px;top:320px;width:537px;height:57px;background:var(--red);color:var(--white);font-size:25px;display:flex;align-items:center;justify-content:center}
.hero-arrow{width:32px;height:32px;background:#222;display:flex;align-items:center;justify-content:center}
/* section headings */
.section-title{left:0;width:1200px;text-align:center;font-size:34px;color:var(--red);letter-spacing:.5px}
.carousel-arrow{width:24px;height:30px}
/* services */
.service{width:290px;text-align:center}
.service-art{margin:0 auto;width:150px;height:160px;background:linear-gradient(135deg,#e01b2f 0%,#c8182a 65%,#cfcfcf 100%)}
.service-name{margin-top:18px;font-size:22px;color:var(--red)}
.service-text{margin:8px auto 0;width:275px;font-size:11.5px;line-height:16px;color:var(--muted)}
.btn-outline{display:inline-block;border:1px solid #999;background:var(--white);color:#444;font-size:12px;letter-spacing:.3px;text-align:center}
/* about */
.about{left:0;top:1138px;width:1200px;height:362px;background:radial-gradient(ellipse at 50% 40%,#3a3a3e 0%,#1c1c1e 70%)}
.about-title{left:145px;top:1210px;font-size:32px;color:var(--white)}
.about-text{left:145px;top:1255px;width:595px;font-size:13px;line-height:24px;color:#e8e8e8}
.about-photo{left:767px;top:1264px;width:288px;height:287px;background:radial-gradient(circle at 50% 40%,#bfe8f6 0%,#5fb6d8 45%,#2b6f93 100%)}
/* resources */
.resource-photo{left:145px;top:1679px;width:456px;height:320px;background:radial-gradient(circle at 55% 35%,#4aa3d6 0%,#1a4d7a 40%,#081629 100%)}
.resource-panel{left:601px;top:1679px;width:454px;height:320px;background:var(--panel);padding:38px 24px 0 24px}
.resource-title{font-size:21px;line-height:29px;color:#333}
.resource-date{margin-top:20px;font-size:14px;color:#333}
.resource-text{margin-top:12px;font-size:11.5px;line-height:19px;color:#555}
/* blog */
.blog{left:0;top:2078px;width:1200px;height:537px;background:var(--soft)}
.post{width:288px}
.post-photo{height:189px}
.post-date{margin-top:16px;font-size:15px;color:#333}
.post-title{margin-top:10px;font-size:17px;line-height:23px;color:var(--red)}
.post-text{margin-top:8px;font-size:11px;line-height:15px;color:#555}
/* contact */
.field{border:1px solid var(--line);background:var(--white);font-size:12px;color:#888;padding:14px 14px}
.submit{left:548px;top:2979px;width:104px;height:41px;background:#2b2b2b;color:var(--white);font-size:12px;display:flex;align-items:center;justify-content:center}
/* footer */
.site-footer{left:0;top:3100px;width:1200px;height:97px;background:#2a2a2a}
.footer-links{left:145px;top:3124px;font-size:11.5px;color:#cfcfcf;word-spacing:2px}
.footer-copy{left:145px;top:3154px;font-size:11.5px;color:#9a9a9a}
.social{width:16px;height:16px;border-radius:50%;background:#8a8a8a}
.live-chat{left:718px;top:3147px;width:271px;height:50px;background:var(--red);color:var(--white);font-size:17px;display:flex;align-items:center;padding:0 18px;gap:10px}
</style>
</head>
<body>

<header class="site-header abs">
  <div class="brand abs"><span class="brand-mark"></span>Quillmarsh</div>
  <nav class="main-nav abs">
    <span class="current" style="left:503px">Home</span>
    <span style="left:589px">Services</span>
    <span style="left:693px">About</span>
    <span style="left:780px">Resources</span>
    <span style="left:897px">Blog</span>
    <span style="left:973px">Contact Us</span>
  </nav>
</header>

<section class="hero abs" role="img" aria-label="Photo of a hand touching a smartphone with security icons over a laptop"></section>
<div class="hero-caption abs">Pellentesque blandit lacus eget nunc faucibus</div>
<div class="hero-arrow abs" style="left:0;top:332px"><svg width="12" height="16"><path d="M9 2 3 8l6 6" stroke="#fff" stroke-width="3" fill="none"/></svg></div>
<div class="hero-arrow abs" style="left:1168px;top:332px"><svg width="12" height="16"><path d="M3 2l6 6-6 6" stroke="#fff" stroke-width="3" fill="none"/></svg></div>

<h2 class="section-title abs" style="top:685px">SERVICES</h2>
<svg class="carousel-arrow abs" style="left:56px;top:891px" viewBox="0 0 24 30"><path d="M16 5 7 15l9 10" stroke="#555" stroke-width="3" fill="none"/></svg>
<svg class="carousel-arrow abs" style="left:1120px;top:891px" viewBox="0 0 24 30"><path d="M8 5l9 10-9 10" stroke="#555" stroke-width="3" fill="none"/></svg>

<div class="service abs" style="left:147px;top:746px">
  <div class="service-art" role="img" aria-label="Service illustration for risk management"></div>
  <div class="service-name">Risk Management</div>
  <p class="service-text">Vestibulum condimentum, risus ut posuere cursus, velit justo accumsan sem, lobortis aliquet metus dui eu libero imperdiet dolor.</p>
  <span class="btn-outline" style="margin-top:12px;width:103px;height:39px;line-height:37px">READ MORE</span>
</div>

<div class="service abs" style="left:460px;top:746px">
  <div class="service-art" role="img" aria-label="Service illustration for security and cyber security"></div>
  <div class="service-name">Security and Cyber Security</div>
  <p class="service-text">Vestibulum condimentum, risus ut posuere cursus, velit justo accumsan sem, lobortis aliquet metus dui eu libero imperdiet dolor.</p>
  <span class="btn-outline" style="margin-top:12px;width:103px;height:39px;line-height:37px">READ MORE</span>
</div>

<div class="service abs" style="left:773px;top:746px">
  <div class="service-art" role="img" aria-label="Service illustration for digital officers"></div>
  <div class="service-name">Digital Officers</div>
  <p class="service-text">Vestibulum condimentum, risus ut posuere cursus, velit justo accumsan sem, lobortis aliquet metus dui eu libero imperdiet dolor.</p>
  <span class="btn-outline" style="margin-top:12px;width:103px;height:39px;line-height:37px">READ MORE</span>
</div>

<section class="about abs" role="img" aria-label="Dark background with a faint network pattern"></section>
<h2 class="about-title abs">ABOUT US</h2>
<p class="about-text abs">Etiam quis aliquet risus. Duis ornare erat eget magna dapibus, in accumsan quam pharetra. Nam tempus, quam in bibendum vulputate, sapien dolor viverra nisl, vitae euismod elit turpis et nulla. Aliquam erat volutpat. Pellentesque blandit lacus eget nunc faucibus, et tincidunt odio viverra. Phasellus consequat sagittis nisi suscipit feugiat. Cras eget leo sed nunc hendrerit ultricies eu at nisl. Praesent iaculis faucibus urna sit amet lacinia. Maecenas consequat justo enim, ac mattis massa imperdiet quis. Fusce eget neque elit. Sed augue orci, elementum in magna congue, tincidunt vulputate erat. Aliquam consectetur orci molestie dictum molestie. Proin eget congue nulla, vel tempor diam.</p>
<div class="about-photo abs" role="img" aria-label="Top-down photo of a person working on a laptop surrounded by glowing cloud network lines"></div>

<h2 class="section-title abs" style="top:1622px">RESOURCES</h2>
<svg class="carousel-arrow abs" style="left:56px;top:1822px" viewBox="0 0 24 30"><path d="M16 5 7 15l9 10" stroke="#555" stroke-width="3" fill="none"/></svg>
<svg class="carousel-arrow abs" style="left:1120px;top:1822px" viewBox="0 0 24 30"><path d="M8 5l9 10-9 10" stroke="#555" stroke-width="3" fill="none"/></svg>
<div class="resource-photo abs" role="img" aria-label="Photo of a hand holding a glowing digital padlock on a dark blue background"></div>
<article class="resource-panel abs">
  <h3 class="resource-title">Aenean facilisis tincidunt lectus dictum luctus eget efficitur ex condimentum</h3>
  <div class="resource-date">15 Feb, 2019</div>
  <p class="resource-text">Pellentesque convallis molestie enim sit amet efficitur. Etiam id imperdiet lectus. Vivamus lacus justo, ultrices nec erat in, euismod iaculis mauris. Vivamus eleifend vitae nulla vel malesuada. In ac malesuada lacus, et consectetur ante. Fusce vitae lectus sit amet mi pulvinar maximus.</p>
  <span class="btn-outline" style="margin-top:18px;width:105px;height:38px;line-height:36px">READ MORE</span>
</article>

<section class="blog abs"></section>
<h2 class="section-title abs" style="top:2149px">BLOG</h2>
<svg class="carousel-arrow abs" style="left:43px;top:2286px" viewBox="0 0 24 30"><path d="M16 5 7 15l9 10" stroke="#555" stroke-width="3" fill="none"/></svg>
<svg class="carousel-arrow abs" style="left:1132px;top:2286px" viewBox="0 0 24 30"><path d="M8 5l9 10-9 10" stroke="#555" stroke-width="3" fill="none"/></svg>

<article class="post abs" style="left:145px;top:2208px">
  <div class="post-photo" role="img" aria-label="Blue digital circuit security graphic" style="background:radial-gradient(circle at 40% 50%,#3aa0e0 0%,#0d3a70 55%,#061a36 100%)"></div>
  <div class="post-date">15 February, 2019</div>
  <h3 class="post-title">Quisque aliquet ex nec est vestibulum pulvinar. Pellentesque convallis.</h3>
  <p class="post-text">Nunc sit amet consequat risus. Curabitur ac elit leo. In eleifend dui tellus, in scelerisque elit porttitor et. Integer eu massa lacinia, lacinia nulla non, volutpat purus.</p>
</article>
<article class="post abs" style="left:456px;top:2208px">
  <div class="post-photo" role="img" aria-label="Hooded figure at a desk with glowing computer screens" style="background:linear-gradient(135deg,#2a4a5e 0%,#102431 50%,#1d4558 100%)"></div>
  <div class="post-date">15 February, 2019</div>
  <h3 class="post-title">Etiam id imperdiet lectus. Vivamus lacus justo, ultrices nec.</h3>
  <p class="post-text">Nunc sit amet consequat risus. Curabitur ac elit leo. In eleifend dui tellus, in scelerisque elit porttitor et. Integer eu massa lacinia, lacinia nulla non, volutpat purus.</p>
</article>
<article class="post abs" style="left:767px;top:2208px">
  <div class="post-photo" role="img" aria-label="Businessman using a tablet with floating security icons" style="background:linear-gradient(135deg,#4b5d70 0%,#6fb7d4 55%,#2d4254 100%)"></div>
  <div class="post-date">15 February, 2019</div>
  <h3 class="post-title">Fusce vitae lectus sit amet mi pulvinar maximus. Aenean placerat.</h3>
  <p class="post-text">Nunc sit amet consequat risus. Curabitur ac elit leo. In eleifend dui tellus, in scelerisque elit porttitor et. Integer eu massa lacinia, lacinia nulla non, volutpat purus.</p>
</article>

<h2 class="section-title abs" style="top:2685px">CONTACT US</h2>
<div class="field abs" style="left:145px;top:2743px;width:296px;height:43px">Name</div>
<div class="field abs" style="left:452px;top:2743px;width:296px;height:43px">Email</div>
<div class="field abs" style="left:757px;top:2743px;width:298px;height:43px">Phone</div>
<div class="field abs" style="left:145px;top:2798px;width:910px;height:160px">Comment</div>
<div class="submit abs">SUBMIT</div>

<footer class="site-footer abs"></footer>
<div class="footer-links abs">Home &nbsp;|&nbsp; Services &nbsp;|&nbsp; About &nbsp;|&nbsp; Resources &nbsp;|&nbsp; Blog &nbsp;|&nbsp; Contact Us</div>
<div class="footer-copy abs">Copyright © 2019 Quillmarsh. &nbsp;All rights reserved.</div>
<div class="social abs" style="left:1002px;top:3139px"></div>
<div class="social abs" style="left:1036px;top:3139px"></div>
<div class="live-chat abs">
  <svg width="18" height="16" viewBox="0 0 18 16"><path d="M2 2h11v8H6l-3 3v-3H2z" fill="#fff"/><path d="M14 5h2v7h-1v2l-2-2H8v-1h6z" fill="#fff"/></svg>
  <span>Live Chat With Us</span>
  <svg style="margin-left:auto" width="10" height="8"><path d="M0 7 5 1l5 6z" fill="#fff"/></svg>
</div>

</body>
</html>
```